Corporate Design für eine Beratungsfirma in der Finanzindustrie gesucht
The design is excellent and we are 100% satisfied. We got all the file formats we wanted to have and velutino gave us every help we needed, after the project was finished. The collaboration was very pleasant.
Zielgruppe
IT Beratung und Softwarelösungen für die Finanzindustrie. Wir bewegen uns ausschliesslich im B2B Bereich (Entscheiderebene).
siehe der Entwurf unserer Homepage: http://71230584.kgv.norvalo-webspace.eu/index-palumo.html
Aufgabenstellung
Da unsere Zielgruppe eher konservativ ist, legen wir großen Wert auf Schlichtheit und Seriosität im Design. Die Farben sollten eher ruhig gehalten sein.

```html
<!DOCTYPE html>
<html lang="de">
<head>
<meta charset="utf-8">
<title>Palumo – Corporate Design</title>
<link href="https://fonts.googleapis.com/css2?family=Source+Sans+3:wght@400;600;700&display=swap" rel="stylesheet">
<style>
:root{
  --navy:#1f3d52;
  --ink:#1d1d1d;
  --muted:#555;
  --paper:#ffffff;
  --frame:#d6d6d6;
  --window:#e6e6e6;
  --stage:#dedede;
  --font:"Source Sans 3", Arial, sans-serif;
}
*{box-sizing:border-box;margin:0;padding:0}
html,body{width:1200px;height:1161px;overflow:hidden;background:var(--paper);font-family:var(--font);color:var(--ink)}
.canvas{position:relative;width:1200px;height:1161px;border:1px solid var(--frame)}
.abs{position:absolute}

/* letterhead */
.letterhead{left:32px;top:36px;width:526px;height:742px;background:var(--paper);border:2px solid #e8e8e8}
.brand{position:absolute;display:flex;flex-direction:column}
.brand-name{font-weight:600;line-height:1;letter-spacing:.5px;display:flex;align-items:center;gap:10px}
.brand-dot{display:inline-block;border-radius:50%;background:currentColor}
.brand-tag{font-weight:400;white-space:nowrap}
.letterhead .brand{left:62px;top:92px;color:var(--navy)}
.letterhead .brand-name{font-size:50px}
.letterhead .brand-dot{width:16px;height:16px}
.letterhead .brand-tag{font-size:10px;color:var(--ink);margin-top:4px;margin-left:26px}
.impressum{position:absolute;right:72px;top:132px;text-align:right;font-size:8.5px;line-height:11.5px}
.impressum p+p{margin-top:11px}
.letter-body{position:absolute;left:60px;top:250px;width:420px;font-size:10px;line-height:14.4px}
.subject{font-weight:700;margin-bottom:30px}
.letter-body p{margin-bottom:14px}
.letter-body .para2{margin-top:28px}
.closing{margin-top:26px}
.signature{font-weight:700;font-size:11.5px}
.footer-rule{position:absolute;left:46px;top:634px;width:442px;height:2px;background:#777}
.footer{position:absolute;left:82px;top:656px;display:flex;gap:22px;font-size:10.5px;color:#444;line-height:12px}
.footer-item{display:flex;align-items:flex-start;gap:7px}
.footer-item svg{flex:none;margin-top:1px}

/* business cards */
.card-stage{left:586px;top:44px;width:586px;height:440px;background:var(--stage)}
.card{position:absolute;width:300px;height:190px}
.card-front{left:30px;top:28px;background:var(--paper)}
.card-front .brand{left:18px;top:16px;color:var(--navy)}
.card-front .brand-name{font-size:18px;gap:5px}
.card-front .brand-dot{width:7px;height:7px}
.card-front .brand-tag{font-size:5px;color:var(--ink)}
.name-band{position:absolute;left:0;top:66px;width:100%;height:36px;background:var(--navy);color:#fff;text-align:center;padding-top:4px}
.name-band strong{display:block;font-size:14px;letter-spacing:1.5px;font-weight:600}
.name-band span{font-size:8px;letter-spacing:.5px}
.card-info{position:absolute;left:18px;top:116px;right:18px;display:flex;justify-content:space-between;font-size:6px;line-height:8px;color:#333}
.card-info b{display:block;font-size:6.5px;border-bottom:1px solid #999;margin-bottom:2px}
.card-back{left:256px;top:222px;background:var(--navy);color:#fff}
.card-back .brand{left:50%;top:50%;transform:translate(-50%,-50%);align-items:center}
.card-back .brand-name{font-size:40px;gap:8px}
.card-back .brand-dot{width:12px;height:12px}
.card-back .brand-tag{font-size:8px;margin-top:3px}

/* envelope */
.envelope{left:574px;top:519px;width:606px;height:267px;border:2px solid #111;background:var(--paper)}
.envelope .brand{left:38px;top:20px;color:var(--navy)}
.envelope .brand-name{font-size:34px;gap:7px}
.envelope .brand-dot{width:11px;height:11px}
.envelope .brand-tag{font-size:7px;color:var(--ink);margin-left:18px;margin-top:2px}
.address-window{position:absolute;left:40px;top:136px;width:203px;height:95px;border-radius:10px;background:var(--window)}

/* brand band */
.brand-band{left:0;top:830px;width:1200px;height:331px;background:var(--navy)}
.brand-band .brand{left:50%;top:50%;transform:translate(-50%,-50%);color:#fff;align-items:center}
.brand-band .brand-name{font-size:78px;gap:14px}
.brand-band .brand-dot{width:22px;height:22px}
.brand-band .brand-tag{font-size:13px;margin-top:8px}
</style>
</head>
<body>
<div class="canvas">

  <section class="abs letterhead" aria-label="Briefbogen">
    <div class="brand">
      <div class="brand-name"><span class="brand-dot"></span>Palumo</div>
      <div class="brand-tag">Consulting | Project Reanimation | Finance IT</div>
    </div>
    <div class="impressum">
      <p>Impressum:<br>Palumo<br>Inhaber: <strong>John Doe</strong><br>Lindenallee 14,&nbsp; D-13189 Berlin</p>
      <p>Telefon: +49.(0)170.402 5518<br>Mail:&nbsp;&nbsp; kontakt@palumo-beratung.de<br>USt-Id-Nr.: DE 48/207/11593</p>
    </div>
    <div class="letter-body">
      <div class="subject">Betreff : Lorem Ipsum</div>
      <p>Sehr geehrte Damen und Herren,</p>
      <p>Lorem ipsum dolor sit amet, cosetetur sadipscing elitr, sed diam nonumy eirmod tempor invidunt ut labore et dolore magna aliquyam erat, sed diam voluptua. At vero eos et accusam et justo duo dolores et ea rebum. Stet clita kasd gubergren, no sea takimata sanctus est Lorem ipsum dolor sit amet. Lorem ipsum color sit amet, consetetur sadiscing elitr, sed diam nonumy eirmod tempor</p>
      <p class="para2">Duis autem vel eum iriure dolor in hendrerit in vulputate velit esse molstie consequat, vel illum dolore eu feugiat nulla facilisis at vero eros et accumsan et ilusto odio dignissim qui blandit preasent uptatum zzril delenit augeu duis dolore te feugiat nulla facilisi. Lorem ipsum dolor sit amet.</p>
      <p class="closing">Mit Freundlichen Gruben</p>
      <p class="signature">John Doe</p>
    </div>
    <div class="footer-rule"></div>
    <div class="footer">
      <div class="footer-item">
        <svg width="11" height="14" viewBox="0 0 11 14" aria-hidden="true"><path d="M5.5 0C2.5 0 0 2.3 0 5.2 0 9 5.5 14 5.5 14S11 9 11 5.2C11 2.3 8.5 0 5.5 0Zm0 7.3a2 2 0 1 1 0-4 2 2 0 0 1 0 4Z" fill="#444"/></svg>
        <span>Talstraße 22<br>60388 Frankfurt</span>
      </div>
      <div class="footer-item">
        <svg width="14" height="11" viewBox="0 0 14 11" aria-hidden="true"><path d="M1 3.5C1 1.5 4 .5 7 .5s6 1 6 3l-2.6.8-.8-1.6H4.4l-.8 1.6Z" fill="#444"/><path d="M3 5h8l1.5 5h-11Z" fill="#444"/><circle cx="7" cy="7.4" r="1.4" fill="#fff"/></svg>
        <span>+49(0)1705521846</span>
      </div>
      <div class="footer-item">
        <svg width="14" height="10" viewBox="0 0 14 10" aria-hidden="true"><rect x=".5" y=".5" width="13" height="9" fill="#444"/><path d="M.5.5 7 6 13.5.5" fill="none" stroke="#fff" stroke-width="1"/></svg>
        <span>kontakt@palumo-beratung.de</span>
      </div>
    </div>
  </section>

  <section class="abs card-stage" aria-label="Visitenkarten">
    <div class="card card-front">
      <div class="brand">
        <div class="brand-name"><span class="brand-dot"></span>Palumo</div>
        <div class="brand-tag">Consulting | Project Reanimation | Finance IT</div>
      </div>
      <div class="name-band"><strong>JOHN DOE</strong><span>Director</span></div>
      <div class="card-info">
        <div><b>Address</b>Lindenallee 14<br>13189 Berlin</div>
        <div><b>Phone / Fax</b>+49 30 4025 518<br>+49 30 4025 519</div>
        <div><b>Email / Site</b>kontakt@palumo.de<br>palumo.de</div>
      </div>
    </div>
    <div class="card card-back">
      <div class="brand">
        <div class="brand-name"><span class="brand-dot"></span>Palumo</div>
        <div class="brand-tag">Consulting | Project Reanimation | Finance IT</div>
      </div>
    </div>
  </section>

  <section class="abs envelope" aria-label="Briefumschlag">
    <div class="brand">
      <div class="brand-name"><span class="brand-dot"></span>Palumo</div>
      <div class="brand-tag">Consulting | Project Reanimation | Finance IT</div>
    </div>
    <div class="address-window"></div>
  </section>

  <section class="abs brand-band" aria-label="Markenauftritt">
    <div class="brand">
      <div class="brand-name"><span class="brand-dot"></span>Palumo</div>
      <div class="brand-tag">Consulting | Project Reanimation | Finance IT</div>
    </div>
  </section>

</div>
</body>
</html>
```